Financial Advisor needs a NEW business card design

We need a new card design as our current design has no white space and clients tend to want to write on the card. I am attaching our current logos and current card design. I have also played with some designs I liked online but don't have the knowledge (or software) to complete the designs in a format that is appropriate for production. I've attached those designs that I liked too. With two office locations and a disclaimer there is a lot of info but we want it to look tidy. We like the deep, rich blue colors and want it to look clean, strong, and modern yet classic.
Business
Included in the attached files

```html
<!DOCTYPE html>
<html lang="en">
<head>
<meta charset="utf-8">
<title>Norwell Financial Advisory – Business Card</title>
<link rel="stylesheet" href="https://fonts.googleapis.com/css2?family=Crimson+Pro:wght@400;600;700&family=Marcellus+SC&display=swap">
<style>
  :root {
    --navy: #0f2d5c;
    --navy-deep: #0a2753;
    --blue-mid: #3f6697;
    --blue-light: #5c82b0;
    --grey: #8d8d8d;
    --white: #ffffff;
    --paper: #ffffff;
  }
  * { margin: 0; padding: 0; box-sizing: border-box; }
  html, body { width: 1200px; height: 900px; overflow: hidden; background: var(--paper); }
  .canvas { position: relative; width: 1200px; height: 900px; }

  /* Front side */
  .card-front {
    position: absolute; left: 46px; top: 31px; width: 703px; height: 422px;
    background: var(--navy-deep); overflow: hidden;
  }
  .front-texture {
    position: absolute; left: 0; top: 22px; width: 703px; height: 300px;
    background: linear-gradient(180deg, var(--blue-mid) 0%, var(--blue-light) 35%, var(--blue-mid) 70%, #34598b 100%);
  }
  .front-name {
    position: absolute; left: 95px; top: 92px;
    color: var(--white); font-family: "Crimson Pro", serif; font-weight: 600;
    font-size: 84px; line-height: 1; white-space: nowrap;
  }
  .front-tag {
    position: absolute; left: 350px; top: 104px; width: 256px; text-align: right;
    color: var(--white); font-family: "Crimson Pro", serif; font-weight: 600;
    font-size: 40px; line-height: 46px; white-space: nowrap;
  }
  .front-rule {
    position: absolute; left: 167px; top: 235px; width: 438px; height: 4px;
    background: var(--white); border-radius: 2px;
  }
  .office {
    position: absolute; top: 330px; width: 340px; text-align: center;
    font-family: "Marcellus SC", serif; font-style: normal; color: var(--white);
    font-size: 22px; line-height: 33px; white-space: nowrap;
  }
  .office-fort-worth { left: 0; }
  .office-plano { left: 350px; }

  /* Back side */
  .back-name {
    position: absolute; left: 497px; top: 508px;
    color: var(--navy); font-family: "Crimson Pro", serif; font-weight: 600;
    font-size: 44px; line-height: 1; white-space: nowrap;
  }
  .back-tag {
    position: absolute; left: 640px; top: 524px; width: 130px; text-align: right;
    color: var(--navy); font-family: "Crimson Pro", serif; font-weight: 600;
    font-size: 21px; line-height: 25px; white-space: nowrap;
  }
  .back-rule {
    position: absolute; left: 540px; top: 594px; width: 230px; height: 4px; background: var(--grey);
  }
  .advisor {
    position: absolute; left: 850px; top: 524px; width: 290px; text-align: center;
    font-family: "Crimson Pro", serif; font-weight: 700; text-transform: uppercase; white-space: nowrap;
  }
  .advisor-name { color: var(--navy); font-size: 36px; line-height: 40px; }
  .advisor-title { color: var(--grey); font-size: 25px; line-height: 28px; }
  .contact-list {
    position: absolute; left: 845px; top: 632px; list-style: none;
    font-family: "Crimson Pro", serif; font-size: 27px; color: var(--navy); white-space: nowrap;
  }
  .contact-list li { display: flex; align-items: center; height: 37px; }
  .contact-list svg { width: 21px; height: 21px; margin-right: 15px; fill: var(--navy); flex: none; }
  .disclaimer {
    position: absolute; left: 600px; top: 826px; width: 430px; text-align: center;
    font-family: "Marcellus SC", serif; font-size: 12.5px; line-height: 16px; color: var(--navy);
  }
</style>
</head>
<body>
<main class="canvas">
  <section class="card-front">
    <div class="front-texture" role="img" aria-label="Deep blue brushed texture background"></div>
    <div class="front-name">Norwell</div>
    <div class="front-tag">FINANCIAL<br>ADVISORY</div>
    <div class="front-rule"></div>
    <address class="office office-fort-worth">4820 Alder Ave., Suite 410<br>Fort Worth, TX 76115</address>
    <address class="office office-plano">220 W. Elm Blvd., Suite 630<br>Plano, TX 75093</address>
  </section>

  <section class="card-back">
    <div class="back-name">Norwell</div>
    <div class="back-tag">FINANCIAL<br>ADVISORY</div>
    <div class="back-rule"></div>

    <div class="advisor">
      <div class="advisor-name">Dan Hartley</div>
      <div class="advisor-title">Financial Advisor</div>
    </div>

    <ul class="contact-list">
      <li><svg viewBox="0 0 24 24"><path d="M6.6 2.5 9.4 6c.4.5.3 1.2-.1 1.6L7.6 9.2c1.2 2.8 3.4 5 6.2 6.3l1.6-1.7c.4-.4 1.1-.5 1.6-.1l3.5 2.8c.5.4.6 1.1.2 1.6l-1.7 2.3c-.5.6-1.3.9-2 .7C9.3 19.4 4.6 14.7 2.9 7c-.2-.8.1-1.5.7-2l2.3-1.7c.2-.3.5-.6.7-.8z"/></svg>817.555.0142 Fort Worth</li>
      <li><svg viewBox="0 0 24 24"><path d="M6.6 2.5 9.4 6c.4.5.3 1.2-.1 1.6L7.6 9.2c1.2 2.8 3.4 5 6.2 6.3l1.6-1.7c.4-.4 1.1-.5 1.6-.1l3.5 2.8c.5.4.6 1.1.2 1.6l-1.7 2.3c-.5.6-1.3.9-2 .7C9.3 19.4 4.6 14.7 2.9 7c-.2-.8.1-1.5.7-2l2.3-1.7c.2-.3.5-.6.7-.8z"/></svg>972.555.0187 Plano</li>
      <li><svg viewBox="0 0 24 24"><path d="M2 6h20v1.2l-10 6.3L2 7.2z"/><path d="M2 9.4l10 6.2 10-6.2V18H2z"/></svg>dan@norwellfa.com</li>
      <li><svg viewBox="0 0 24 24"><g stroke="#0f2d5c" stroke-width="1.6" fill="none"><circle cx="12" cy="12" r="9"/><ellipse cx="12" cy="12" rx="4" ry="9"/><path d="M3 12h18M5 7h14M5 17h14"/></g></svg>www.norwellfa.com</li>
    </ul>

    <p class="disclaimer">Investment advisory services offered through Meridian Private Capital, LLC, an SEC registered investment advisor</p>
  </section>
</main>
</body>
</html>
```